Präsentationsvorlagen/Workbook für Coaching - Yoga - Training
Zielgruppe
Coaching - Yoga - Training, d.h. Yogaunterricht, Einzelcoaching, Seminare und Workshops rund um das Thema Stress/Resilienz/Achtsamkeit
Zielgruppe sind einerseits überwiegend Frauen, aber auch Firmenkunden, die für ihre Mitarbeiter Seminare und Yoga anbieten.
Aufgabenstellung
Ich benötige einen professionellen ppt Auftritt für Präsentationen/Workbooks mit meinen Firmenfarben (grau, weiß, rosa, beige) in den mein Logo integriert ist.
Das Design sollte dem Thema entsprechend 'warm' sein aber die nötige Professionalität für Firmenkunden ausstrahlen.

```html
<!DOCTYPE html>
<html lang="de">
<head>
<meta charset="utf-8">
<title>Lena Marwitz – Präsentationsvorlage</title>
<link href="https://fonts.googleapis.com/css2?family=Barlow:wght@400;500;700;800&family=Cinzel:wght@400;500&family=Libre+Baskerville:wght@400;700&display=swap" rel="stylesheet">
<style>
:root{
  --pink:#b5588a;
  --pink-soft:#e7c6d7;
  --plum-top:#9b5a82;
  --plum-bottom:#3b2633;
  --ink:#3a3a3a;
  --text:#8a8a8a;
  --strip:#f4f4f4;
  --page:#dcdcdc;
  --white:#ffffff;
  --tag:#6d6d6d;
  --dark:#3c3c3c;
}
*{margin:0;padding:0;box-sizing:border-box}
html,body{width:700px;height:1200px;overflow:hidden}
body{background:var(--page);font-family:"Barlow",sans-serif;color:var(--text);position:relative}
.slide{position:absolute;width:332px;height:187px;background:var(--white);overflow:hidden;box-shadow:0 2px 6px rgba(0,0,0,.08)}
.c1{left:12px}.c2{left:356px}
.r1{top:205px}.r2{top:406px}.r3{top:607px}.r4{top:808px}
.strip{position:absolute;left:0;top:0;width:16px;height:100%;background:var(--strip)}
.strip .mark{position:absolute;left:0;top:0;width:16px;height:16px;background:var(--pink)}
.strip .rule{position:absolute;left:8px;top:90px;width:.5px;height:30px;background:#c8c8c8}
.strip .url{position:absolute;left:3px;top:150px;font-size:3px;color:#999;transform:rotate(-90deg);transform-origin:left top;white-space:nowrap;letter-spacing:.2px}
.strip .dots{position:absolute;left:6.5px;bottom:8px;display:flex;flex-direction:column;gap:2px}
.dot{width:3px;height:3px;border-radius:50%;background:var(--pink-soft)}
.dot.on{background:var(--pink)}
.pageno{position:absolute;right:6px;bottom:6px;width:12px;height:9px;background:#7a7a7a;color:#fff;font-size:3px;display:flex;align-items:center;justify-content:center}
.abs{position:absolute}
.photo{position:absolute}
.title{font-family:"Libre Baskerville",serif;font-weight:700;color:var(--pink);font-size:13px;letter-spacing:-.3px;line-height:1}
.title .dark{color:var(--ink)}
.sub{font-size:4px;color:var(--tag);margin-top:3px}
.tdots{display:flex;gap:3px;margin-top:6px}
.tdots .dot{width:4px;height:4px}
.body{font-size:3.6px;line-height:1.7;color:var(--text)}
.body p+p{margin-top:4px}
.btn{position:absolute;height:11px;padding:0 6px;border:.6px solid var(--pink);color:var(--pink);font-size:3.6px;letter-spacing:.2px;display:flex;align-items:center;text-transform:uppercase}

/* cover */
.cover{background:linear-gradient(180deg,var(--plum-top),#6b3d58 45%,var(--plum-bottom))}
.cover .photo{inset:0;background:radial-gradient(ellipse at 50% 70%,rgba(30,20,25,.45),transparent 60%),linear-gradient(180deg,rgba(190,120,160,.25),rgba(40,25,35,.3))}
.menu{position:absolute;left:10px;top:10px;width:8px}
.menu i{display:block;height:.8px;background:#fff;margin-bottom:2px}
.menu i:last-child{width:5px}
.cover .url-top{position:absolute;right:18px;top:8px;font-size:3px;color:#f0dbe6}
.cover .ring{position:absolute;left:141px;top:42px;width:50px;height:50px;border:2px solid #fff;border-radius:50%}
.cover .name{position:absolute;left:0;right:0;top:100px;text-align:center;font-family:"Cinzel",serif;color:#fff;font-size:19px;letter-spacing:.5px;line-height:1}
.cover .tagline{position:absolute;left:0;right:0;top:120px;text-align:center;font-family:"Cinzel",serif;color:#fff;font-size:7.5px;letter-spacing:.4px}
.cover .copy{position:absolute;left:16px;bottom:12px;font-size:3px;color:#fff}
.cover .line{position:absolute;left:70px;right:16px;bottom:13.5px;height:.5px;background:rgba(255,255,255,.6)}

/* toc */
.toc-head{left:52px;top:28px}
.toc-rule{left:121px;top:52px;width:65px;height:.6px;background:#bbb}
.toc-item{position:absolute;width:80px}
.toc-item .num{font-family:"Barlow",sans-serif;font-weight:500;font-size:10px;color:var(--ink);line-height:1;display:inline-block;vertical-align:top}
.toc-item .num::after{content:"";display:block;width:11px;height:1px;background:var(--pink);margin-top:2px}
.toc-item .lab{display:inline-block;font-size:3.6px;font-weight:500;color:var(--ink);letter-spacing:.3px;line-height:1.4;margin-left:5px;margin-top:2.5px;text-transform:uppercase}
.toc-item .desc{font-size:3.4px;line-height:1.4;color:#999;margin-top:5px}
.faint-ring{position:absolute;border:6px solid #f4f4f4;border-radius:50%}
</style>
</head>
<body>

<!-- 1 cover -->
<section class="slide c1 r1 cover">
  <div class="photo" role="img" aria-label="Foto einer meditierenden Frau vor Holzgeländer im Abendlicht, in Rosé getönt"></div>
  <div class="menu"><i></i><i></i></div>
  <div class="url-top">www.lenamarwitz.org</div>
  <div class="ring"></div>
  <div class="name">LENA MARWITZ</div>
  <div class="tagline">COACHING - YOGA - TRAINING</div>
  <div class="copy">© 2023 All Rights Reserved</div>
  <div class="line"></div>
</section>

<!-- 2 table of content -->
<section class="slide c2 r1">
  <div class="strip"><div class="mark"></div><div class="rule"></div><div class="url">www.lenamarwitz.org</div><div class="dots"><span class="dot"></span><span class="dot on"></span></div></div>
  <div class="faint-ring" style="left:210px;top:12px;width:110px;height:110px"></div>
  <div class="abs title toc-head" style="font-size:12px;line-height:1.25">Table<br><span class="dark">Of Content.</span></div>
  <div class="abs toc-rule"></div>
  <div class="toc-item" style="left:52px;top:80px"><span class="num">01</span><span class="lab">One content<br>title text here</span><div class="desc">Lorem ipsum dolor sit amet, duis<br>at consetetur sadipscing.</div></div>
  <div class="toc-item" style="left:139px;top:80px"><span class="num">02</span><span class="lab">Two content<br>title text here</span><div class="desc">Lorem ipsum dolor sit amet, duis<br>at consetetur sadipscing.</div></div>
  <div class="toc-item" style="left:226px;top:80px"><span class="num">03</span><span class="lab">Three content<br>title text here</span><div class="desc">Lorem ipsum dolor sit amet, duis<br>at consetetur sadipscing.</div></div>
  <div class="toc-item" style="left:52px;top:131px"><span class="num">04</span><span class="lab">Four content<br>title text here</span><div class="desc">Lorem ipsum dolor sit amet, duis<br>at consetetur sadipscing.</div></div>
  <div class="toc-item" style="left:139px;top:131px"><span class="num">05</span><span class="lab">Five content<br>title text here</span><div class="desc">Lorem ipsum dolor sit amet, duis<br>at consetetur sadipscing.</div></div>
  <div class="toc-item" style="left:226px;top:131px"><span class="num">06</span><span class="lab">Six content<br>title text here</span><div class="desc">Lorem ipsum dolor sit amet, duis<br>at consetetur sadipscing.</div></div>
  <div class="pageno">2</div>
</section>

<!-- 3 welcome -->
<section class="slide c1 r2">
  <div class="strip"><div class="mark"></div><div class="rule"></div><div class="url">www.lenamarwitz.org</div><div class="dots"><span class="dot"></span><span class="dot on"></span></div></div>
  <div class="photo" role="img" aria-label="Schreibtisch mit Notizbuch und Grünpflanze in hellem Licht" style="left:0;top:0;width:332px;height:187px;background:linear-gradient(135deg,#e9efec,#cfd8d3 55%,#9aa59f);clip-path:polygon(78% 0,100% 0,100% 100%,45% 100%)"></div>
  <div class="abs" style="left:49px;top:37px;width:125px">
    <div class="title">Welcome <span class="dark">Message</span></div>
    <div class="sub">_ Lorem ipsum dolor sit amet consectetur adipiscing elit</div>
    <div class="tdots"><span class="dot on"></span><span class="dot"></span><span class="dot"></span></div>
    <div class="body" style="margin-top:7px;text-align:justify"><p>Schön, dass Du da bist! Ich bin Lena und begleite Menschen ganzheitlich auf dem Weg zu Klarheit und Zufriedenheit. Yoga, Coaching und Training verbinde ich zu einer wunderbaren Kombination auf körperlicher und mentaler Ebene.</p></div>
    <div class="body" style="margin-top:8px;font-style:italic;padding-left:16px">Ich begleite Dich gern auf Deinem Weg.</div>
    <div role="img" aria-label="Handschriftliche Unterschrift" style="margin:6px 0 0 82px;width:40px;height:8px;background:#f3e4ec"></div>
  </div>
  <div class="photo" role="img" aria-label="Porträtfoto der Coachin" style="left:191px;top:67px;width:56px;height:56px;border-radius:50%;border:3px solid #fff;background:radial-gradient(circle at 50% 40%,#c9a58c,#6e5647);box-shadow:0 1px 4px rgba(0,0,0,.15)"></div>
  <div class="pageno">3</div>
</section>

<!-- 4 coaching -->
<section class="slide c2 r2">
  <div class="strip"><div class="mark"></div><div class="rule"></div><div class="url">www.lenamarwitz.org</div><div class="dots"><span class="dot"></span><span class="dot on"></span></div></div>
  <div class="photo" role="img" aria-label="Coachin im blauen Kleid sitzt im Korbsessel" style="left:48px;top:0;width:98px;height:105px;background:linear-gradient(160deg,#eae6e2,#b8b2ae 50%,#3f4f70)"></div>
  <div class="abs" style="left:49px;top:114px">
    <div class="title">Coaching</div>
    <div class="sub">_ Zurück zur Selbstfürsorge und Selbstbestimmtheit</div>
    <div class="tdots"><span class="dot on"></span><span class="dot"></span><span class="dot"></span></div>
  </div>
  <div class="abs body" style="left:161px;top:34px;width:100px">
    <p>Wo stehst Du heute? Und wo möchtest Du hin? Coaching ist ein lösungsorientierter Prozess, der Dir in herausfordernden Lebenssituationen hilft und Dir Klarheit schenkt.</p>
    <p>Mein fachliches Wissen kombiniere ich mit ausgeprägtem Einfühlungsvermögen in einem sicheren und vertrauensvollen Rahmen.</p>
  </div>
  <div class="btn" style="left:161px;top:149px">Erstgespräch vereinbaren</div>
  <div class="photo" role="img" aria-label="Glühbirne vor Sonnenuntergang am Meer" style="left:274px;top:0;width:58px;height:187px;background:linear-gradient(180deg,#efe3b8,#d9a072 40%,#6d6a70 70%,#2d3340)"></div>
  <div class="pageno">4</div>
</section>

<!-- 5 yoga -->
<section class="slide c1 r3">
  <div class="strip"><div class="mark"></div><div class="rule"></div><div class="url">www.lenamarwitz.org</div><div class="dots"><span class="dot"></span><span class="dot on"></span></div></div>
  <div class="abs" style="left:48px;top:51px">
    <div class="title">Yoga</div>
    <div class="sub">_ Innere Ruhe und Steigerung des Wohlbefindens</div>
    <div class="tdots"><span class="dot on"></span><span class="dot"></span><span class="dot"></span></div>
  </div>
  <div class="photo" role="img" aria-label="Silhouette einer meditierenden Person auf Holzterrasse im Gegenlicht" style="left:166px;top:0;width:138px;height:83px;background:linear-gradient(180deg,#8a8a86,#4b4640 55%,#2b2520)"></div>
  <div class="photo" role="img" aria-label="Lachende Frau mit Mütze im Wald" style="left:48px;top:93px;width:98px;height:68px;background:linear-gradient(135deg,#5f6540,#8a7258 55%,#3d3a2c)"></div>
  <div class="abs body" style="left:166px;top:96px;width:132px">
    <p>Yoga unterstützt meine Arbeit als Coachin auf wunderbare Art und Weise. Viele Jahre habe ich Yoga gelernt und bleibe immer eine Lernende.</p>
    <p>Daher biete ich Kurse und Workshops für Firmen, Erwachsene, Kinder und Familien an.</p>
  </div>
  <div class="btn" style="left:166px;top:149px;width:59px;justify-content:center">Kurse anfragen</div>
  <div class="pageno">5</div>
</section>

<!-- 6 training -->
<section class="slide c2 r3">
  <div class="strip"><div class="mark"></div><div class="rule"></div><div class="url">www.lenamarwitz.org</div><div class="dots"><span class="dot"></span><span class="dot on"></span></div></div>
  <div class="photo" role="img" aria-label="Fenster mit Kissen auf der Fensterbank" style="left:48px;top:0;width:57px;height:161px;background:linear-gradient(180deg,#d7e2e6,#b3c7b8 45%,#8f7a6a 85%,#5b3b2a)"></div>
  <div class="photo" role="img" aria-label="Porträt der Trainerin in weißer Bluse" style="left:106px;top:0;width:89px;height:119px;background:linear-gradient(180deg,#f1f3f5,#d9d4cf 50%,#efeeec)"></div>
  <div class="abs" style="left:113px;top:127px">
    <div class="title">Training</div>
    <div class="sub">_ Mit Freude Neues erlernen!</div>
    <div class="tdots"><span class="dot on"></span><span class="dot"></span><span class="dot"></span></div>
  </div>
  <div class="abs body" style="left:209px;top:40px;width:92px">
    <p>Suchen Sie eine kompetente Partnerin für ökonomische und psychologische Lehrinhalte? Dann sprechen Sie mich gerne an!</p>
    <p>Als zertifizierte Trainerin der Erwachsenenbildung liebe ich es, Menschen zu entwickeln und zu begleiten.</p>
  </div>
  <div class="btn" style="left:209px;top:150px;width:59px;justify-content:center">Training anfragen</div>
  <div class="pageno">6</div>
</section>

<!-- 7 nordic walking -->
<section class="slide c1 r4">
  <div class="strip"><div class="mark"></div><div class="rule"></div><div class="url">www.lenamarwitz.org</div><div class="dots"><span class="dot"></span><span class="dot on"></span></div></div>
  <div class="photo" role="img" aria-label="Gelbe Wanderwegweiser vor Felswand" style="left:48px;top:26px;width:149px;height:42px;background:linear-gradient(90deg,#56655e,#8b8f86 45%,#6f7769)"></div>
  <div class="abs" style="left:48px;top:73px">
    <div class="title">Nordic <span class="dark">walking</span></div>
    <div class="sub">_ Körper und Geist im Einklang mit der Natur</div>
    <div class="tdots"><span class="dot on"></span><span class="dot"></span><span class="dot"></span></div>
  </div>
  <div class="abs body" style="left:48px;top:111px;width:150px">
    <p>Langjährigen Walkern wie Anfängern zeige ich in meinen Kursen die korrekte Technik mit vielen Übungen auf schönen Strecken.</p>
    <p>Die Bewegung in der Natur lässt sich gut mit Coaching verknüpfen.</p>
  </div>
  <div class="btn" style="left:48px;top:150px;width:59px;justify-content:center">Kurse entdecken</div>
  <div class="photo" role="img" aria-label="Frau mit Walkingstöcken an einem Baum im Herbstpark" style="left:210px;top:26px;width:93px;height:135px;background:linear-gradient(120deg,#8a9a5a,#5d5540 50%,#7a6a4a)"></div>
  <div class="pageno">7</div>
</section>

<!-- 8 break time -->
<section class="slide c2 r4" style="background:var(--dark)">
  <div class="photo" role="img" aria-label="Unscharfer dunkler Schreibtisch mit Notizbuch" style="inset:0;background:radial-gradient(ellipse at 70% 90%,#5a5a5a,#3a3a3a 60%,#2f2f2f)"></div>
  <div class="abs" style="left:79px;top:36px;font-weight:800;font-size:30px;color:#fff;letter-spacing:-.5px;line-height:1">Break</div>
  <svg class="abs" style="left:172px;top:32px" width="90" height="52" viewBox="0 0 90 52" aria-hidden="true">
    <path d="M6 0H84a6 6 0 0 1 6 6V30a6 6 0 0 1-6 6H20L0 52V6a6 6 0 0 1 6-6z" fill="#b5588a"/>
  </svg>
  <div class="abs" style="left:180px;top:36px;font-weight:800;font-size:30px;color:var(--ink);letter-spacing:-.5px;line-height:1">Time</div>
  <div class="abs" style="left:80px;top:72px;font-size:5px;color:#fff"><b>Let's take</b> a 30-minute break</div>
  <div class="abs" style="left:54px;top:100px;width:224px;height:61px;background:#fff;border-radius:4px;display:flex">
    <div style="width:110px;border-right:.5px solid #e2e2e2;padding:10px 0 0 17px;font-size:4.6px;font-weight:700;color:var(--ink);line-height:2.9">
      <div><span style="color:var(--pink);margin-right:6px">•</span>Title text here</div>
      <div><span style="color:var(--pink);margin-right:6px">•</span>Title text here</div>
      <div><span style="color:var(--pink);margin-right:6px">•</span>Title text here</div>
    </div>
    <div style="flex:1;text-align:center;padding-top:14px">
      <div style="font-weight:800;font-size:19px;color:var(--pink);line-height:1">09.35</div>
      <div style="font-size:6.5px;color:#666;margin-top:3px">Next Discussion</div>
    </div>
  </div>
</section>

</body>
</html>
```